Tervane Electronic Security Web Site

We need a web site for our new company based in Sydney Australia.
We specialize in consulting supplying and installing electronic security systems. These include CCTV, Access control, Alarms, Intercom and Network cabling.
We pride our selves in giving our customers peace of mind giving back security and freedom to our customers. We pride in customer service quality products and expertise with and we do the job as though it is for our personal friends and family.
We need to be able to edit web site contents and update information.

```html
<!DOCTYPE html>
<html lang="en">
<head>
<meta charset="utf-8">
<title>Tervane Electronic Security</title>
<link rel="stylesheet" href="https://fonts.googleapis.com/css2?family=Source+Sans+Pro:ital,wght@0,400;0,600;0,700;1,400;1,600&display=swap">
<style>
:root{
  --navy:#34496b;
  --gold:#e5a11a;
  --header-bg:#f4f4f4;
  --footer-bg:#3e3e3e;
  --text:#555;
  --dark:#1a1a1a;
  --blue:#1a8fd0;
  --band-bg:#f2f2f2;
}
*{margin:0;padding:0;box-sizing:border-box}
html,body{width:1200px;height:1200px;overflow:hidden;background:#fff;font-family:"Source Sans Pro",Arial,sans-serif;color:var(--text)}
.page{position:relative;width:1200px;height:1200px}
.site-header{position:absolute;top:0;left:0;width:1200px;height:80px;background:var(--header-bg)}
.brand{position:absolute;left:108px;top:16px;display:flex;align-items:center;gap:10px}
.brand-mark{width:44px;height:44px;border:3px solid var(--navy);background:#fff}
.brand-name{font-weight:700;font-size:14px;line-height:16px;color:var(--navy);text-transform:uppercase;width:100px}
.main-nav{position:absolute;top:0;left:472px;display:flex;height:80px}
.nav-item{height:80px;padding:30px 0 0;text-align:center;text-transform:uppercase;font-size:13px;font-weight:600;color:var(--dark);white-space:nowrap}
.nav-item small{display:block;text-transform:none;font-size:10px;font-weight:400;color:#888;margin-top:2px}
.nav-item.active{background:var(--navy);color:#fff}
.nav-item.active small{color:#c9d2e0}
.hero{position:absolute;top:80px;left:0;width:1200px;height:332px;background:linear-gradient(100deg,#f6f6f6 0%,#e6e6e6 45%,#d0d0d0 100%)}
.hero-photo{position:absolute;left:130px;top:60px;width:365px;height:250px;background:linear-gradient(180deg,#3a3a3a 0%,#1d1d1d 65%,#e2e2e2 100%);border-radius:4px}
.cert-badges{position:absolute;left:135px;top:274px;display:flex;gap:14px}
.cert-badges span{width:30px;height:26px;border-radius:4px;background:#8a8a8a}
.cert-badges span:last-child{border-radius:50%;width:26px}
.hero-title{position:absolute;left:505px;top:66px;width:505px;text-align:center;font-size:26px;line-height:30px;font-weight:600;color:#111}
.accessories{position:absolute;left:555px;top:183px;display:flex;gap:8px}
.accessories span{width:72px;height:72px;border-radius:50%;background:radial-gradient(circle,#bbb 0%,#e8e8e8 55%,#fff 70%);border:2px solid #e3e3e3}
.price{position:absolute;left:818px;top:168px;color:var(--blue);font-weight:700;white-space:nowrap}
.price .cur{font-size:26px;vertical-align:bottom}
.price .main{font-size:80px;line-height:82px;letter-spacing:-2px}
.price .cents{font-size:24px}
.price-old{position:absolute;left:975px;top:226px;font-size:16px;color:#999;text-decoration:line-through}
.buy-now{position:absolute;left:961px;top:271px;width:133px;height:32px;border-radius:16px;background:linear-gradient(#2a8fe0,#0d5fa8);color:#fff;font-weight:700;font-size:19px;line-height:31px;text-align:center;white-space:nowrap}
.slide-arrow{position:absolute;top:126px;width:40px;height:52px;background:#3f3f3f}
.slide-arrow.prev{left:60px}.slide-arrow.next{left:1100px}
.services{position:absolute;top:426px;left:0;width:1200px}
.service{position:absolute;top:0;width:204px;height:210px}
.welcome{position:absolute;top:668px;left:100px;width:1000px;text-align:center}
.welcome h1{font-size:25px;font-weight:700;color:var(--navy);line-height:32px}
.welcome h1 em{font-style:normal;color:var(--gold)}
.welcome p{font-size:13px;line-height:21px;margin-top:2px}
.cta-band{position:absolute;top:771px;left:100px;width:1000px;height:97px;background:var(--band-bg)}
.cta-band h2{position:absolute;left:23px;top:18px;width:800px;font-size:27px;font-weight:700;color:#4a4a4a;white-space:nowrap;overflow:hidden}
.cta-band p{position:absolute;left:23px;top:56px;width:800px;text-align:center;font-size:14px;white-space:nowrap}
.cta-button{position:absolute;left:846px;top:27px;width:132px;height:48px;background:var(--navy);color:#fff;font-weight:700;font-size:13px;line-height:18px;text-align:center;padding-top:6px;text-transform:uppercase}
.site-footer{position:absolute;top:868px;left:0;width:1200px;height:138px;background:var(--footer-bg);color:#eee;font-style:italic;overflow:hidden}
.footer-col h3{font-size:18px;font-weight:400;color:var(--gold);margin-bottom:8px;white-space:nowrap}
.contact{position:absolute;left:60px;top:16px;width:400px;text-align:center;font-size:13px;line-height:23px;white-space:nowrap}
.contact a{color:var(--gold);text-decoration:none}
.contact .note{font-weight:600;margin-top:3px}
.social{position:absolute;left:468px;top:15px;width:222px}
.social h3{text-align:center}
.social-icons{display:flex;gap:17px;margin-top:16px}
.social-icons span{width:26px;height:26px;border-radius:50%;background:#6b6b6b}
.social-icons span:first-child{background:var(--gold)}
.newsletter{position:absolute;left:783px;top:16px;width:315px}
.subscribe-form{display:flex;border:2px solid #fff;height:36px;background:#fff}
.subscribe-form .field{flex:1;font-size:11px;color:#bbb;padding:9px 10px}
.subscribe-form .btn{width:91px;background:var(--gold);color:#fff;font-size:14px;text-align:center;line-height:32px}
.copyright{font-size:11px;text-align:center;margin-top:9px;color:#fff;white-space:nowrap}
</style>
</head>
<body>
<div class="page">
  <header class="site-header">
    <div class="brand"><span class="brand-mark"></span><span class="brand-name">Tervane Electronic Security</span></div>
    <nav class="main-nav">
      <div class="nav-item active" style="width:88px">Main Page<small>welcome</small></div>
      <div class="nav-item" style="width:126px">About Us<small>who we are</small></div>
      <div class="nav-item" style="width:80px">Services<small>what we do</small></div>
      <div class="nav-item" style="width:138px">Customers<small>testimonials</small></div>
      <div class="nav-item" style="width:86px">Our Blog<small>latest news</small></div>
      <div class="nav-item" style="width:140px">Contact Us<small>stay in touch</small></div>
    </nav>
  </header>

  <section class="hero">
    <div class="hero-photo" role="img" aria-label="Four bullet CCTV cameras standing on a network DVR recorder"></div>
    <div class="cert-badges"><span></span><span></span><span></span></div>
    <h2 class="hero-title">Home 4CH CCTV DVR Security Camera Surveillance System No Hard Drive</h2>
    <div class="accessories">
      <span role="img" aria-label="Network cable"></span>
      <span role="img" aria-label="Camera connectors"></span>
      <span role="img" aria-label="Power adapter"></span>
    </div>
    <div class="price"><span class="cur">£</span><span class="main">99</span><span class="cents">.89</span></div>
    <div class="price-old">£109.99</div>
    <div class="buy-now">Buy Now &gt;&gt;</div>
    <div class="slide-arrow prev"><svg width="40" height="52"><polyline points="24,14 13,26 24,38" fill="none" stroke="#ddd" stroke-width="1.5"/></svg></div>
    <div class="slide-arrow next"><svg width="40" height="52"><polyline points="16,14 27,26 16,38" fill="none" stroke="#ddd" stroke-width="1.5"/></svg></div>
  </section>

  <section class="services">
    <svg class="service" style="left:125px" viewBox="0 0 204 210"><defs><clipPath id="c1"><circle cx="102" cy="104" r="92"/></clipPath></defs>
      <circle cx="102" cy="104" r="100" fill="#fff" stroke="var(--navy)" stroke-width="3"/>
      <circle cx="102" cy="72" r="48" fill="#e9edf3" role="img" aria-label="CCTV camera icon"/>
      <rect x="0" y="130" width="204" height="80" fill="var(--gold)" clip-path="url(#c1)"/>
      <text x="102" y="172" text-anchor="middle" font-family="Source Sans Pro, sans-serif" font-weight="700" font-size="34" fill="#fff">CCTV</text></svg>
    <svg class="service" style="left:385px" viewBox="0 0 204 210"><defs><clipPath id="c2"><circle cx="102" cy="104" r="92"/></clipPath></defs>
      <circle cx="102" cy="104" r="100" fill="#fff" stroke="var(--navy)" stroke-width="3"/>
      <circle cx="102" cy="72" r="48" fill="#e9edf3" role="img" aria-label="House with alarm icon"/>
      <rect x="0" y="130" width="204" height="80" fill="var(--gold)" clip-path="url(#c2)"/>
      <text x="102" y="165" text-anchor="middle" font-family="Source Sans Pro, sans-serif" font-weight="700" font-size="30" fill="#fff">ALARM</text>
      <text x="102" y="183" text-anchor="middle" font-family="Source Sans Pro, sans-serif" font-size="15" fill="#fff">SYSTEM</text></svg>
    <svg class="service" style="left:635px" viewBox="0 0 204 210"><defs><clipPath id="c3"><circle cx="102" cy="104" r="92"/></clipPath></defs>
      <circle cx="102" cy="104" r="100" fill="#fff" stroke="var(--navy)" stroke-width="3"/>
      <circle cx="102" cy="72" r="48" fill="#e9edf3" role="img" aria-label="Keypad access panel icon"/>
      <rect x="0" y="130" width="204" height="80" fill="var(--gold)" clip-path="url(#c3)"/>
      <text x="102" y="165" text-anchor="middle" font-family="Source Sans Pro, sans-serif" font-weight="700" font-size="30" fill="#fff">ACCESS</text>
      <text x="102" y="183" text-anchor="middle" font-family="Source Sans Pro, sans-serif" font-size="15" fill="#fff">CONTROL</text></svg>
    <svg class="service" style="left:885px" viewBox="0 0 204 210"><defs><clipPath id="c4"><circle cx="102" cy="104" r="92"/></clipPath></defs>
      <circle cx="102" cy="104" r="100" fill="#fff" stroke="var(--navy)" stroke-width="3"/>
      <circle cx="102" cy="72" r="48" fill="#e9edf3" role="img" aria-label="Group of users icon"/>
      <rect x="0" y="130" width="204" height="80" fill="var(--gold)" clip-path="url(#c4)"/>
      <text x="102" y="165" text-anchor="middle" font-family="Source Sans Pro, sans-serif" font-weight="700" font-size="30" fill="#fff">ACCESS</text>
      <text x="102" y="183" text-anchor="middle" font-family="Source Sans Pro, sans-serif" font-size="15" fill="#fff">CONTROL</text></svg>
  </section>

  <section class="welcome">
    <h1>welcome to <em>Tervane Electronic Security</em></h1>
    <p>Lorem ipsum dolor sit amet, consectetuer adipiscing elit. Aenean commodo ligula eget dolor. Aenean massa. Cum sociis natoque penatibus et magnis dis parturient montes, nascetur ridiculus mus. Donec quam felis, ultricies nec, pellentesque eu, pretium quis, sem. Nulla consequat massa quis enim. Donec pede justo, fringilla vel, aliquet nec, vulputate eget, arcu. In enim justo, rhoncus ut, imperdiet a, venenatis vitae, justo.</p>
  </section>

  <section class="cta-band">
    <h2>CCTV, Access control, Alarms, Intercom and Network cabling.</h2>
    <p>Lorem ipsum dolor sit amet, consectetuer adipiscing elit. Aenean commodo ligula eget dolor. Aenean massa.</p>
    <div class="cta-button">Get in touch<br>with us</div>
  </section>

  <footer class="site-footer">
    <div class="footer-col contact">
      <h3>Contact us</h3>
      <div>Email us: <a>info@tervanesecurity.example</a></div>
      <div>SMS/WhatsApp/Call Us: <a>+61.2000.1234 / +61.2000.5678</a></div>
      <div class="note">We are more than happy to discuss food with you!</div>
    </div>
    <div class="footer-col social">
      <h3>Social Media:</h3>
      <div class="social-icons"><span></span><span></span><span></span><span></span><span></span><span></span></div>
    </div>
    <div class="footer-col newsletter">
      <h3>Subscribe Our Newsletters</h3>
      <div class="subscribe-form"><span class="field">your e-mail address</span><span class="btn">subscribe</span></div>
      <div class="copyright">Copyright © 2014 by tervanesecurity.example</div>
    </div>
  </footer>
</div>
</body>
</html>
```